Kings of Polished Fog*

I am looking for a book cover which will really pop. Working title: Kings of Polished Fog (or K.P.F. for short) The concept behind the book is: education is too expensive, screwed up, and basically failing us, and even an MBA is not worth it's name anymore! How a BS is Brilliantly Stupid, a BA is great to be a Broke Artist, an MA is Mostly Antiquated and a MS Mastered Something? ...you get the point, basically I'll be ripping into a whole bunch of degree types, then walking you through what you should actually learn from an MBA. It is going to be written with a fair bit of humor, while still being fact driven. Target audience is working professionals who are considering an MBA, or have one and want a $15 refresher of all they spent $90k+ on. No color scheme is requested, Since i do like to allow creativity to flow!

Book size 5" by 8" and ebook. Author is: R.J. Halvorsen size format attached.

Went on vacation/holiday

• K.P.F. (but can be an emphasises in the Kings of Polished Fog title.
• If you look at "Lanterns over Elm Creek: a gentle account of harvest seasons on the northern farm" on brindlecart, you can see a blue/silver/white color scheme I liked in the past - but dont take that as a must by any means, the second choice was a completely different (red and white) scheme

```html
<!DOCTYPE html>
<html lang="en">
<head>
<meta charset="utf-8">
<title>Kings of Polished Fog — Book Cover</title>
<link rel="stylesheet" href="https://fonts.googleapis.com/css2?family=Anton&family=Oswald:wght@700&display=swap">
<style>
  :root {
    --page: #ffffff;
    --forest-deep: #16301c;
    --forest: #1e4a38;
    --teal-glow: #2e8c88;
    --teal-band: #2b8580;
    --gold-light: #fdf59a;
    --gold: #d9b44a;
    --gold-deep: #b57a34;
    --title-white: #ffffff;
    --title-gold: #e4cf6c;
    --badge-fill: #7e8a86;
    --cap-fill: #2f8a83;
    --shadow: rgba(0, 0, 0, 0.75);
  }
  html, body {
    margin: 0;
    padding: 0;
    width: 1200px;
    height: 1200px;
    overflow: hidden;
    background: var(--page);
  }
  .canvas {
    position: relative;
    width: 1200px;
    height: 1200px;
  }
  .book-cover {
    position: absolute;
    left: 334px;
    top: 124px;
    width: 559px;
    height: 894px;
    display: block;
  }
  .title-main, .title-end {
    font-family: "Anton", "Oswald", sans-serif;
    fill: var(--title-white);
  }
  .title-middle {
    font-family: "Anton", "Oswald", sans-serif;
    fill: var(--title-gold);
  }
  .badge-initials {
    font-family: "Anton", "Oswald", sans-serif;
    fill: var(--title-white);
    font-size: 50px;
    letter-spacing: 2px;
  }
  .author-name {
    font-family: "Oswald", sans-serif;
    font-weight: 700;
    fill: var(--title-white);
    font-size: 32px;
  }
</style>
</head>
<body>
<main class="canvas">
  <svg class="book-cover" viewBox="0 0 559 894" xmlns="http://www.w3.org/2000/svg" aria-labelledby="cover-title">
    <title id="cover-title">Kings of Polished Fog by R.J. Halvorsen</title>
    <defs>
      <radialGradient id="base-glow" cx="162" cy="372" r="520" gradientUnits="userSpaceOnUse">
        <stop offset="0" stop-color="var(--teal-glow)"/>
        <stop offset="0.45" stop-color="var(--forest)"/>
        <stop offset="1" stop-color="var(--forest-deep)"/>
      </radialGradient>
      <linearGradient id="gold-sweep" x1="0" y1="0" x2="1" y2="1">
        <stop offset="0" stop-color="var(--gold)"/>
        <stop offset="0.5" stop-color="var(--gold-light)"/>
        <stop offset="1" stop-color="var(--gold)"/>
      </linearGradient>
      <linearGradient id="gold-low" x1="0" y1="0" x2="1" y2="1">
        <stop offset="0" stop-color="var(--gold-deep)"/>
        <stop offset="0.6" stop-color="var(--gold-light)"/>
        <stop offset="1" stop-color="var(--gold)"/>
      </linearGradient>
      <linearGradient id="badge-ring" x1="0" y1="0" x2="0" y2="1">
        <stop offset="0" stop-color="var(--gold-deep)"/>
        <stop offset="1" stop-color="var(--gold-light)"/>
      </linearGradient>
      <radialGradient id="badge-inner" cx="0.5" cy="0.5" r="0.5">
        <stop offset="0" stop-color="var(--teal-glow)"/>
        <stop offset="1" stop-color="var(--forest-deep)"/>
      </radialGradient>
      <path id="badge-arc" d="M 60 204 A 124 124 0 0 0 308 204"/>
      <filter id="drop" x="-10%" y="-10%" width="130%" height="140%">
        <feDropShadow dx="4" dy="5" stdDeviation="1.5" flood-color="#000" flood-opacity="0.75"/>
      </filter>
    </defs>

    <!-- background -->
    <rect class="cover-base" width="559" height="894" fill="url(#base-glow)"/>

    <!-- top-right sweeps -->
    <path class="sweep-teal-top" d="M 42 0 C 250 10, 470 110, 559 292 L 559 0 Z" fill="var(--teal-band)"/>
    <path class="sweep-gold-top" d="M 162 0 C 330 20, 500 90, 559 188 L 559 0 Z" fill="url(#gold-sweep)"/>

    <!-- bottom-left sweeps -->
    <path class="sweep-teal-low" d="M 0 540 C 60 700, 250 830, 426 894 L 0 894 Z" fill="var(--teal-band)" opacity="0.85"/>
    <path class="sweep-dark-low" d="M 0 600 C 80 740, 240 840, 380 894 L 0 894 Z" fill="var(--forest)" opacity="0.7"/>
    <path class="sweep-gold-low" d="M 0 772 C 90 840, 210 880, 322 894 L 0 894 Z" fill="url(#gold-low)"/>

    <!-- badge -->
    <g class="badge">
      <circle cx="184" cy="204" r="148" fill="url(#badge-ring)"/>
      <circle cx="184" cy="204" r="138" fill="url(#badge-inner)"/>
      <rect class="badge-mascot" x="110" y="80" width="150" height="200" rx="40"
            fill="var(--badge-fill)" opacity="0.55" role="img"
            aria-label="Cartoon sheep mascot standing in the badge"/>
      <text class="badge-initials" filter="url(#drop)">
        <textPath href="#badge-arc" startOffset="50%" text-anchor="middle">K.P.F.</textPath>
      </text>
    </g>

    <!-- title -->
    <text class="title-main" x="46" y="476" font-size="134" textLength="472" lengthAdjust="spacingAndGlyphs" filter="url(#drop)">KINGS</text>
    <text class="title-middle" x="46" y="556" font-size="68" textLength="475" lengthAdjust="spacingAndGlyphs" filter="url(#drop)">OF POLISHED</text>
    <rect class="title-cap" x="446" y="552" width="84" height="34" rx="3"
          fill="var(--cap-fill)" role="img" aria-label="Graduation cap resting on the last letter"/>
    <text class="title-end" x="516" y="676" font-size="120" text-anchor="end" textLength="194" lengthAdjust="spacingAndGlyphs" filter="url(#drop)">FOG</text>

    <!-- author -->
    <text class="author-name" x="514" y="836" text-anchor="end" textLength="232" lengthAdjust="spacingAndGlyphs" filter="url(#drop)">R.J. Halvorsen</text>
  </svg>
</main>
</body>
</html>
```